Business Card Design for Toriven

I've already got the logo, but I'd like to see some interesting designs.

I don't want anything to complex. I like it simple,yet innovative, like the logo.

My business is System Administration for small to medium size businesses, so that will be my main target audience.
Updates

hey all, the png has been uploaded.

Hey all,

If you are submitting the back side of the card, I'd like the top bit of the card to be Toriven Solutions and the logo, the bottom of the card the website, with a white background.

The middle I'd like to leave blank for a quote that will be printed on each card.

Thanks!

Dale

Industry/Entity Type

Business

```html
<!DOCTYPE html>
<html lang="en">
<head>
<meta charset="utf-8">
<title>Toriven Solutions – Business Card</title>
<link rel="stylesheet" href="https://fonts.googleapis.com/css2?family=Source+Sans+3:wght@400;600;700&display=swap">
<style>
  :root {
    --backdrop: #b57a4c;
    --card: #ffffff;
    --brand-blue: #2a70ad;
    --bright-blue: #2b9ad8;
    --deep-blue: #1f5f9c;
    --slate: #58595b;
    --ink: #3f4246;
    --muted: #6b6e72;
  }
  * { margin: 0; padding: 0; box-sizing: border-box; }
  html, body {
    width: 1200px; height: 417px; overflow: hidden;
    background: var(--backdrop);
    font-family: "Source Sans 3", Arial, sans-serif;
  }
  .canvas { position: relative; width: 1200px; height: 417px; }
  .card {
    position: absolute; width: 526px; height: 300px;
    background: var(--card); border-radius: 14px; overflow: hidden;
    box-shadow: 0 3px 8px rgba(0,0,0,.35);
  }
  .card--front { left: 42px; top: 52px; }
  .card--back { left: 613px; top: 50px; }

  .brand { position: absolute; display: flex; align-items: center; color: var(--brand-blue); font-weight: 600; }
  .brand__dot { border-radius: 50%; background: var(--brand-blue); flex: none; }
  .brand__text { display: flex; flex-direction: column; line-height: 1; }
  .brand__name { letter-spacing: -0.5px; }
  .brand__sub { letter-spacing: 0.5em; }

  .card--front .brand { left: 52px; top: 44px; }
  .card--front .brand__dot { width: 66px; height: 66px; margin-right: 47px; }
  .card--front .brand__name { font-size: 50px; }
  .card--front .brand__sub { font-size: 14px; margin-top: 2px; }

  .card--back .brand { left: 172px; top: 26px; }
  .card--back .brand__dot { width: 42px; height: 42px; margin-right: 22px; }
  .card--back .brand__name { font-size: 34px; }
  .card--back .brand__sub { font-size: 9px; }

  .person { position: absolute; left: 368px; top: 79px; font-size: 17px; color: var(--brand-blue); white-space: nowrap; }
  .person__name { font-weight: 700; }
  .person__title { font-weight: 400; font-size: 14px; color: var(--muted); }

  .contacts { position: absolute; left: 97px; top: 154px; list-style: none; font-size: 13.5px; color: var(--ink); }
  .contacts li { display: flex; align-items: center; height: 16.5px; }
  .contacts svg { width: 11px; height: 11px; margin-right: 8px; fill: var(--brand-blue); }

  .accent-band {
    position: absolute; left: 0; right: 0; top: 222px; height: 12px;
    background: linear-gradient(90deg, var(--deep-blue), var(--bright-blue));
  }
  .base-band { position: absolute; left: 0; right: 0; top: 234px; bottom: 0; background: var(--slate); }

  .address { position: absolute; left: 362px; top: 242px; color: #fff; font-size: 13.5px; line-height: 19px; }

  .website { position: absolute; left: 0; right: 0; top: 266px; text-align: center; font-size: 13px; letter-spacing: 0.2em; color: var(--muted); }
</style>
</head>
<body>
<div class="canvas">

  <section class="card card--front">
    <div class="accent-band" role="img" aria-label="Decorative blue wave band"></div>
    <div class="base-band"></div>

    <div class="brand">
      <span class="brand__dot"></span>
      <span class="brand__text">
        <span class="brand__name">toriven</span>
        <span class="brand__sub">solutions</span>
      </span>
    </div>

    <p class="person"><span class="person__name">YOUR NAME,</span> <span class="person__title">Title</span></p>

    <ul class="contacts">
      <li><svg viewBox="0 0 12 12"><path d="M3 1l2 2-1 1.5c.6 1.4 1.6 2.4 3 3L8.5 6.5l2 2-1.5 2C5 10 2 7 1.5 2.5z"/></svg>123-456-7890</li>
      <li><svg viewBox="0 0 12 12"><path d="M1 7h10v3H1zM3 3h6l1.5 4h-9z"/></svg>123-456-7890</li>
      <li><svg viewBox="0 0 12 12"><path d="M1 3h10v7H1z"/></svg>info@torivenmail.com</li>
      <li><svg viewBox="0 0 12 12"><circle cx="6" cy="6" r="5"/></svg>www.torivensite.com</li>
    </ul>

    <p class="address">Street Name, City Name<br>State, City Zip 123 4560</p>
  </section>

  <section class="card card--back">
    <div class="brand">
      <span class="brand__dot"></span>
      <span class="brand__text">
        <span class="brand__name">toriven</span>
        <span class="brand__sub">solutions</span>
      </span>
    </div>
    <p class="website">www.torivensite.com</p>
  </section>

</div>
</body>
</html>
```